New counselling and hypnotherapy business

I'd like a flyer which is relevant to people who want support and to improve their wellbeing which follows the same theme as my website: http://larkmoretherapy.plumweave.com
And emphasise that whatever the area of concern, development or growth and I can tailor my knowledge and skills to help.

I'd like to use the same logo and my emphasis is to draw the audience in...therapy and counselling is for people who are "stuck" and having a difficult time...it can also be useful has a personal development tool.

Hypnotherapy

```html
<!DOCTYPE html>
<html lang="en">
<head>
<meta charset="utf-8">
<title>Larkmore Counselling &amp; Hypnotherapy – Flyer</title>
<link rel="stylesheet" href="https://fonts.googleapis.com/css2?family=Roboto+Condensed:ital,wght@0,300;0,400;0,700;1,700&display=swap">
<style>
  :root {
    --backdrop: #e6cbe8;
    --plum: #5f2160;
    --plum-deep: #4a174b;
    --plum-light: #8b3f88;
    --glow: #ffffff;
    --ink-light: #ffffff;
    --bar-red: #e2302e;
    --bar-green: #8cc63f;
    --bar-yellow: #e6bf27;
    --bar-dark: #231223;
    --footer: #2a0f2b;
    --logo-ink: #6a2a69;
  }
  * { margin: 0; padding: 0; box-sizing: border-box; }
  html, body { width: 1200px; height: 1200px; overflow: hidden; }
  body {
    background: var(--backdrop);
    font-family: "Roboto Condensed", "Arial Narrow", sans-serif;
    position: relative;
  }
  .flyer {
    position: absolute;
    left: 252px; top: 43px;
    width: 864px; height: 1118px;
    background: linear-gradient(180deg, var(--plum) 0%, var(--plum) 60%, var(--plum-deep) 100%);
    overflow: hidden;
    color: var(--ink-light);
    box-shadow: 0 10px 30px rgba(60, 10, 60, 0.35);
  }
  .flyer__header-wave {
    position: absolute; left: 0; top: 0;
    width: 864px; height: 320px;
  }
  .brand {
    position: absolute;
    left: 40px; top: 40px;
    width: 320px; height: 280px;
    background: radial-gradient(ellipse at 50% 50%, var(--glow) 0%, rgba(255,255,255,0.95) 35%, rgba(255,255,255,0.4) 62%, rgba(255,255,255,0) 75%);
  }
  .brand__name {
    position: absolute;
    left: 78px; top: 140px;
    width: 200px;
    color: var(--logo-ink);
    font-weight: 400;
    font-size: 26px;
    line-height: 1.05;
    letter-spacing: 0.5px;
  }
  .brand__mark {
    position: absolute;
    left: 138px; top: 78px;
    width: 40px; height: 40px;
    border-radius: 50%;
    background: var(--logo-ink);
  }
  .therapist-photo {
    position: absolute;
    left: 441px; top: 34px;
    width: 123px; height: 127px;
    background: linear-gradient(180deg, #e9e4df 0%, #d8c2b3 55%, #c4474f 100%);
    border: 1px solid rgba(255,255,255,0.6);
  }
  .credentials {
    position: absolute;
    left: 586px; top: 58px;
    font-size: 40px;
    line-height: 52px;
    font-weight: 400;
  }
  .tagline {
    position: absolute;
    left: 442px; top: 168px;
    font-size: 38px;
    letter-spacing: -0.3px;
    font-weight: 400;
    white-space: nowrap;
  }
  .headline {
    position: absolute;
    font-weight: 400;
    white-space: nowrap;
    font-size: 38px;
    letter-spacing: -0.3px;
  }
  .headline strong {
    font-weight: 400;
    font-size: 57px;
  }
  .headline--support { left: 219px; top: 310px; }
  .headline--wellbeing { left: 297px; top: 396px; }
  .hero-photo {
    position: absolute;
    left: 8px; top: 367px;
    width: 400px; height: 640px;
    background: radial-gradient(ellipse at 55% 50%, #a565a3 0%, #7c3a7b 45%, rgba(95,33,96,0) 75%);
  }
  .focus-areas {
    position: absolute;
    left: 431px; top: 547px;
    width: 433px;
    list-style: none;
  }
  .focus-areas li {
    height: 68px;
    padding-left: 19px;
    font-size: 38px;
    letter-spacing: -0.3px;
    line-height: 68px;
    color: var(--ink-light);
    border-bottom: 1px solid rgba(0,0,0,0.25);
    white-space: nowrap;
  }
  .focus-areas .is-red { background: var(--bar-red); }
  .focus-areas .is-green { background: var(--bar-green); }
  .focus-areas .is-yellow { background: var(--bar-yellow); }
  .focus-areas .is-dark { background: var(--bar-dark); padding-left: 22px; }
  .hook {
    position: absolute;
    left: 0; width: 906px; top: 868px;
    text-align: center;
    font-weight: 700;
    font-style: italic;
    font-size: 40px;
    letter-spacing: -0.5px;
  }
  .contact {
    position: absolute;
    left: 0; width: 906px;
    text-align: center;
    white-space: nowrap;
  }
  .contact--phone { top: 943px; font-size: 37px; }
  .contact--email { top: 1003px; font-size: 26px; }
  .footer-band {
    position: absolute;
    left: 0; bottom: 0;
    width: 864px; height: 58px;
    background: var(--footer);
    font-size: 20px;
    line-height: 58px;
    padding-left: 48px;
    white-space: nowrap;
  }
</style>
</head>
<body>
  <article class="flyer">
    <svg class="flyer__header-wave" viewBox="0 0 864 320" aria-hidden="true">
      <path d="M0 0 H864 V250 C700 280 520 250 380 240 C240 232 120 250 0 290 Z" fill="#7b3379"/>
      <path d="M380 240 C520 250 700 280 864 250" stroke="#9a5397" stroke-width="2" fill="none"/>
    </svg>

    <div class="brand">
      <span class="brand__mark"></span>
      <p class="brand__name">LARKMORE<br>Counselling &amp;<br>Hypnotherapy</p>
    </div>

    <div class="therapist-photo" role="img" aria-label="Portrait photo of the therapist"></div>
    <p class="credentials">Trusted<br>Professional</p>
    <p class="tagline">An approach tailored to you</p>

    <h1 class="headline headline--support">People who want <strong>support</strong></h1>
    <p class="headline headline--wellbeing">and to improve their <strong>wellbeing</strong></p>

    <div class="hero-photo" role="img" aria-label="Photo of a young woman sitting hugging her knees, looking troubled"></div>

    <ul class="focus-areas">
      <li class="is-red">Clarify</li>
      <li class="is-green">Growth and development</li>
      <li class="is-yellow">Explore</li>
      <li class="is-dark">Behaviour change</li>
    </ul>

    <p class="hook">"Stuck" and having a difficult time...</p>
    <p class="contact contact--phone">Call Us Now&nbsp; 07700 900418</p>
    <p class="contact contact--email">Email.larkmoretherapy@mailbeam.com</p>

    <footer class="footer-band">Address : Larkmore Counselling &amp; Hypnotherapy, 12B, Mill Lane,&nbsp; Eastmoor West Dunley DN4 7QR</footer>
  </article>
</body>
</html>
```